Business card with logo for a family psychologist

I need a business card for my private practice in the urban Chicago area as a psychologist. I see families and individuals who are going through difficult times - divorce, separation, illness, or trauma. I want to project hopefulness, competence, and caring.

Target Market(s)

Adults, other professionals - such as physicans and lawyers

Industry/Entity Type

Health Care

Contact Information for Business Card

Front should have my name and credentials; back should have location information including my email, phone

Font styles to use
Serif
Decorative
Script

Requirements
Must have
• Unique logo
Should not have
• No pictures or icons of people; no black

```html
<!DOCTYPE html>
<html lang="en">
<head>
<meta charset="utf-8">
<title>Dana Mercer, Ph.D. — Business Card</title>
<link href="https://fonts.googleapis.com/css2?family=Alegreya:ital,wght@1,400&family=Gentium+Book+Plus&display=swap" rel="stylesheet">
<style>
  :root {
    --page-bg: #ecebe8;
    --silver-light: #ffffff;
    --silver-mid: #ececec;
    --silver-dark: #c9c9c9;
    --ink-blue: #1f4f96;
    --band-top: #2a9fd0;
    --band-mid: #1a73b5;
    --band-deep: #1d3f86;
    --text-dark: #2b2b2b;
    --mist: #d9d9d9;
  }
  * { margin: 0; padding: 0; box-sizing: border-box; }
  html, body { width: 934px; height: 1200px; overflow: hidden; background: var(--page-bg); }
  .canvas { position: relative; width: 934px; height: 1200px; }

  .card {
    position: absolute;
    width: 710px;
    height: 411px;
    overflow: hidden;
    background: linear-gradient(90deg, var(--silver-dark) 0%, var(--silver-mid) 18%, var(--silver-light) 45%, var(--silver-light) 75%, var(--silver-mid) 100%);
    box-shadow: 0 4px 14px rgba(0,0,0,0.18);
  }
  .card-front { left: 110px; top: 96px; }
  .card-back { left: 117px; top: 602px; }
  .card svg.shapes { position: absolute; inset: 0; }

  .tree-decoration {
    position: absolute;
    background: radial-gradient(ellipse at center, rgba(255,255,255,0.9) 0%, rgba(225,225,225,0.55) 55%, rgba(225,225,225,0) 75%);
  }
  .card-front .tree-decoration { left: 555px; top: 20px; width: 155px; height: 280px; }
  .card-back .tree-decoration { left: 0; top: 118px; width: 155px; height: 293px; }

  .script {
    font-family: "Alegreya", Georgia, serif;
    font-style: italic;
    font-weight: 400;
    position: absolute;
    white-space: nowrap;
  }
  .logo-mark {
    position: absolute; left: 185px; top: 121px;
    width: 100px; height: 100px; border-radius: 50%;
    background: linear-gradient(180deg, var(--band-top), var(--band-deep));
  }
  .front-name { left: 304px; top: 150px; font-size: 31px; color: var(--ink-blue); }
  .front-title { left: 0; width: 710px; text-align: center; top: 330px; font-size: 27px; color: #ffffff; }

  .back-name { left: 0; width: 710px; text-align: center; top: 52px; font-size: 34px; color: #ffffff; }
  .back-title { left: 192px; top: 171px; font-size: 27px; color: var(--ink-blue); }

  .contact-list { position: absolute; left: 192px; top: 234px; list-style: none;
    font-family: "Gentium Book Plus", Georgia, serif; font-size: 21px; color: var(--text-dark); line-height: 26px; }
  .contact-item { position: relative; padding-left: 43px; }
  .contact-item svg { position: absolute; left: 0; }
  .contact-address svg { top: 4px; }
  .contact-phone { margin-top: 16px; }
  .contact-phone svg { top: 2px; }
  .contact-email { margin-top: 21px; }
  .contact-email svg { top: 6px; }
</style>
</head>
<body>
<main class="canvas">

  <section class="card card-front" aria-label="Card front">
    <div class="tree-decoration" role="img" aria-label="Faint decorative tree illustration"></div>
    <svg class="shapes" width="710" height="411" viewBox="0 0 710 411">
      <defs>
        <linearGradient id="band-front" x1="0" y1="0" x2="0" y2="1">
          <stop offset="0" stop-color="var(--band-top)"/>
          <stop offset="0.5" stop-color="var(--band-mid)"/>
          <stop offset="1" stop-color="var(--band-deep)"/>
        </linearGradient>
        <linearGradient id="rule-front" x1="0" y1="0" x2="1" y2="0">
          <stop offset="0" stop-color="#d8d8d8"/>
          <stop offset="0.5" stop-color="#8f8f8f"/>
          <stop offset="1" stop-color="#d0d0d0"/>
        </linearGradient>
      </defs>
      <path d="M0 298 Q355 260 710 292 L710 411 L0 411 Z" fill="url(#rule-front)"/>
      <path d="M0 306 Q355 270 710 302 L710 411 L0 411 Z" fill="url(#band-front)"/>
    </svg>
    <div class="logo-mark" aria-hidden="true"></div>
    <div class="script front-name">Dana Mercer, Ph.D.</div>
    <div class="script front-title">Licensed Clinical Psychologist</div>
  </section>

  <section class="card card-back" aria-label="Card back">
    <div class="tree-decoration" role="img" aria-label="Faint decorative tree illustration"></div>
    <svg class="shapes" width="710" height="411" viewBox="0 0 710 411">
      <defs>
        <linearGradient id="band-back" x1="0" y1="0" x2="0" y2="1">
          <stop offset="0" stop-color="var(--band-deep)"/>
          <stop offset="0.5" stop-color="var(--band-mid)"/>
          <stop offset="1" stop-color="var(--band-top)"/>
        </linearGradient>
        <linearGradient id="rule-back" x1="0" y1="0" x2="1" y2="0">
          <stop offset="0" stop-color="#d8d8d8"/>
          <stop offset="0.5" stop-color="#8f8f8f"/>
          <stop offset="1" stop-color="#d0d0d0"/>
        </linearGradient>
      </defs>
      <path d="M0 0 L710 0 L710 112 Q355 150 0 112 Z" fill="url(#rule-back)"/>
      <path d="M0 0 L710 0 L710 104 Q355 140 0 104 Z" fill="url(#band-back)"/>
    </svg>
    <div class="script back-name">Dana Mercer, Ph.D.</div>
    <div class="script back-title">Licensed Clinical Psychologist</div>
    <ul class="contact-list">
      <li class="contact-item contact-address">
        <svg width="22" height="32" viewBox="0 0 22 32" aria-hidden="true">
          <path d="M11 1 C5 1 1 5.5 1 11 C1 18 11 31 11 31 C11 31 21 18 21 11 C21 5.5 17 1 11 1 Z" fill="var(--ink-blue)"/>
          <circle cx="11" cy="11" r="4" fill="#ffffff"/>
        </svg>
        240 W. Lakeview Suite 815<br>Chicago, Illinois 60610
      </li>
      <li class="contact-item contact-phone">
        <svg width="24" height="26" viewBox="0 0 24 26" aria-hidden="true">
          <path d="M6 1 L10 7 L7 10 C8 14 11 18 15 20 L18 17 L23 21 L20 25 C10 24 2 15 1 5 Z" fill="var(--ink-blue)"/>
        </svg>
        312-555-0148
      </li>
      <li class="contact-item contact-email">
        <svg width="30" height="20" viewBox="0 0 30 20" aria-hidden="true">
          <rect x="1.5" y="1.5" width="27" height="17" rx="2" fill="none" stroke="var(--ink-blue)" stroke-width="2.5"/>
          <path d="M2 3 L15 12 L28 3" fill="none" stroke="var(--ink-blue)" stroke-width="2.5"/>
        </svg>
        drdanamercer@mail.com
      </li>
    </ul>
  </section>

</main>
</body>
</html>
```